Business card design needed

A business card and logo for my energy healing practice Tarrawin's Healing Spring. It should match my website www.tarrawinshealingspring-example.com in colours and atmosphere. It should look at bit rustic in combination with nature linking in with the natural healing techniques I offer in a heritage country town in NSW Australia. My business also includes a directory of other health and healing practitioners 'The Spring'. It would be nice if a graphic impression of the attached picture of the water feature in my front yard can be used.

Industry/Entity Type

Health

Contact Information for Business Card

Tarrawin's Healing Spring, Delphine Ashcroft, 14 Larchfield St, Millbrook Vale NSW 2799, M. 0491 363 718, info@tarrawinshealingspring-example.com, www.tarrawinshealingspring-example.com,
GENTLE HEALING - ROOTED IN NATURE
Facebook/Twitter see Capital Renewal

```html
<!DOCTYPE html>
<html lang="en">
<head>
<meta charset="utf-8">
<title>Tarrawin's Healing Spring – Business Card</title>
<link href="https://fonts.googleapis.com/css2?family=Parisienne&family=Mulish:wght@400;600&display=swap" rel="stylesheet">
<style>
  :root {
    --page-bg: #e9ecec;
    --teal-deep: #1f3c45;
    --teal-mid: #3c6672;
    --teal-soft: #6f97a2;
    --mist: #b9cfd5;
    --mist-light: #d3e2e6;
    --ink: #2c4650;
    --white: #f4f8f9;
    --script: "Parisienne", cursive;
    --sans: "Mulish", sans-serif;
  }
  * { box-sizing: border-box; margin: 0; padding: 0; }
  html, body { width: 1200px; height: 1000px; overflow: hidden; }
  body { background: var(--page-bg); position: relative; font-family: var(--sans); }

  .card {
    position: absolute;
    width: 600px;
    height: 343px;
    overflow: hidden;
    box-shadow: 0 6px 18px rgba(0,0,0,.18);
  }

  /* Front */
  .card--front {
    left: 170px; top: 110px;
    background: linear-gradient(180deg, var(--teal-deep) 0%, var(--teal-mid) 22%, var(--teal-soft) 42%, var(--mist) 62%, var(--mist-light) 72%);
    text-align: center;
  }
  .front__headline {
    font-family: var(--script);
    color: var(--white);
    font-size: 50px;
    font-weight: 400;
    position: absolute; left: 0; right: 0; top: 34px;
  }
  .front__services {
    position: absolute; left: 0; right: 0; top: 142px;
    color: var(--ink);
    font-size: 17px;
    line-height: 26px;
  }
  .front__landscape {
    position: absolute; left: 0; right: 0; bottom: 0; height: 120px;
    background: linear-gradient(180deg, rgba(111,151,162,0) 0%, var(--teal-soft) 35%, var(--teal-mid) 65%, var(--teal-deep) 100%);
  }
  .front__tagline {
    position: absolute; left: 0; right: 0; bottom: 18px;
    color: var(--white);
    font-size: 17px;
    letter-spacing: 1.2px;
  }

  /* Back */
  .card--back {
    left: 430px; top: 520px;
    background: linear-gradient(180deg, var(--teal-deep) 0%, var(--teal-mid) 100%);
  }
  .back__photo {
    position: absolute; left: 0; top: 0; bottom: 0; width: 292px;
    background: linear-gradient(180deg, var(--teal-soft) 0%, #9db9c1 45%, var(--mist-light) 100%);
  }
  .back__brand {
    position: absolute; left: 10px; width: 272px; top: 196px;
    text-align: center;
    color: var(--ink);
  }
  .brand__name {
    font-family: var(--sans);
    font-size: 27px;
    line-height: 34px;
    font-weight: 400;
  }
  .brand__tagline {
    font-size: 11px;
    letter-spacing: .6px;
    margin-top: 10px;
  }
  .back__details {
    position: absolute; left: 304px; top: 14px; right: 6px;
    color: var(--white);
  }
  .details__name {
    font-family: var(--script);
    font-size: 40px;
    line-height: 40px;
    font-weight: 400;
    margin-bottom: 16px;
  }
  .details__list { list-style: none; font-size: 12.5px; line-height: 22px; white-space: nowrap; }
  .details__list .strong { font-weight: 600; }
  .social { display: flex; align-items: center; gap: 7px; }
  .social__dot { width: 14px; height: 14px; border-radius: 50%; background: var(--white); flex: none; }
</style>
</head>
<body>

<section class="card card--front">
  <h1 class="front__headline">A sanctuary for your health</h1>
  <p class="front__services">
    Sessions – Workshops – Directory<br>
    www.tarrawinshealingspring-example.com<br>
    www.capitalrenewal-example.com.au
  </p>
  <div class="front__landscape" role="img" aria-label="Misty blue mountain ranges fading into the distance"></div>
  <p class="front__tagline">GENTLE HEALING - ROOTED IN NATURE</p>
</section>

<section class="card card--back">
  <div class="back__photo" role="img" aria-label="Soft blue-toned view of a cottage garden with a stone water feature"></div>
  <div class="back__brand">
    <h2 class="brand__name">Tarrawin's<br>Healing Spring</h2>
    <p class="brand__tagline">GENTLE HEALING - ROOTED IN NATURE</p>
  </div>
  <div class="back__details">
    <h3 class="details__name">Delphine<br>Ashcroft</h3>
    <ul class="details__list">
      <li>14 Larchfield Street</li>
      <li>Millbrook Vale NSW 2799</li>
      <li class="strong">0491 363 718</li>
      <li class="strong">info@tarrawinshealingspring-example.com</li>
      <li class="strong">www.tarrawinshealingspring-example.com</li>
      <li class="social"><span class="social__dot"></span>capitalrenewal</li>
      <li class="social"><span class="social__dot"></span>@capitalrenewal</li>
      <li class="social"><span class="social__dot"></span>capitalrenewal</li>
    </ul>
  </div>
</section>

</body>
</html>
```